Business Card Design

We are looking for a double sided business card.

On one side would be our logo

On the Other Side

Daniel Workby
Sales and Marketing

Phone/Text Logo and 530-471-6328
Email Logo and info@gildedcritters.example
Website Logo and www.gildedcritters.example
Facebook Logo and gilded critters
Instagram Logo and gilded_critters

Target Market(s)

Pet owners

Contact Information for Business Card

In project description

Requirements
Must have
• Logo

```html
<!DOCTYPE html>
<html lang="en">
<head>
<meta charset="utf-8">
<title>Gilded Critters – Business Card</title>
<link href="https://fonts.googleapis.com/css2?family=Lato:wght@300;400;700;900&display=swap" rel="stylesheet">
<style>
  :root {
    --stage-top: #3a3a3c;
    --stage-bottom: #141414;
    --card: #232325;
    --orange: #f7931e;
    --amber: #f9b21a;
    --yellow: #f5d416;
    --silver: #d9d9db;
    --silver-dark: #9a9a9c;
    --white: #f2f2f2;
    --icon-grey: #8c8c8e;
  }
  * { box-sizing: border-box; margin: 0; padding: 0; }
  html, body { width: 1200px; height: 952px; overflow: hidden; }
  body {
    background: radial-gradient(ellipse at 55% 45%, var(--stage-top), var(--stage-bottom) 75%);
    font-family: "Lato", sans-serif;
    position: relative;
  }
  .card {
    position: absolute;
    width: 620px;
    height: 354px;
    background: var(--card);
    border-radius: 4px;
    overflow: hidden;
    box-shadow: 0 18px 40px rgba(0,0,0,.55);
  }
  .card--logo { left: 500px; top: 92px; }
  .card--contact { left: 80px; top: 506px; }

  /* brand lockup (shared) */
  .brand {
    position: absolute;
    display: flex;
    flex-direction: column;
    align-items: center;
  }
  .brand__row { display: flex; align-items: center; gap: 12px; }
  .brand__dot {
    width: 22px; height: 22px; border-radius: 50%;
    background: var(--orange);
  }
  .brand__name {
    font-weight: 900;
    font-size: 34px;
    letter-spacing: 1px;
    color: var(--silver);
    text-transform: uppercase;
    line-height: 1;
  }
  .brand__url {
    margin-top: 10px;
    font-size: 10px;
    letter-spacing: 3px;
    color: var(--orange);
    text-transform: uppercase;
  }

  /* logo side */
  .card--logo .brand { left: 0; right: 0; top: 148px; }
  .tab {
    position: absolute;
    width: 150px; height: 50px;
    border-radius: 8px;
    background: linear-gradient(90deg, var(--orange), var(--yellow) 55%, var(--orange));
  }
  .tab--top { left: 60px; top: -20px; }
  .tab--bottom { right: -14px; bottom: 22px; }

  /* contact side */
  .card--contact .brand { left: 34px; top: 86px; align-items: flex-start; }
  .card--contact .brand__name { font-size: 26px; }
  .card--contact .brand__url { font-size: 9px; letter-spacing: 2.5px; }

  .person {
    position: absolute;
    right: 36px; top: 54px;
    text-align: right;
  }
  .person__name {
    font-size: 27px;
    color: var(--orange);
    letter-spacing: 1px;
    text-transform: uppercase;
    font-weight: 400;
  }
  .person__name strong { font-weight: 900; }
  .person__role {
    display: inline-block;
    margin-top: 4px;
    font-size: 16px;
    font-weight: 300;
    color: var(--white);
    padding-bottom: 6px;
    border-bottom: 1.5px solid var(--white);
  }

  .contacts {
    position: absolute;
    right: 36px; top: 182px;
    list-style: none;
    display: flex;
    flex-direction: column;
    align-items: flex-end;
    gap: 6px;
  }
  .contacts li {
    display: flex;
    align-items: center;
    gap: 8px;
    font-size: 14px;
    font-weight: 400;
    color: var(--white);
  }
  .icon {
    width: 18px; height: 18px;
    border-radius: 3px;
    background: var(--amber);
    display: flex; align-items: center; justify-content: center;
  }
  .icon svg { width: 12px; height: 12px; }
  .icon--social { background: var(--icon-grey); }
  .icons { display: flex; gap: 4px; }

  .band {
    position: absolute;
    left: 0; right: 64px; bottom: 34px;
    height: 10px;
    display: flex;
  }
  .band__warm { flex: 0 0 48%; background: linear-gradient(90deg, var(--orange), var(--yellow) 60%, var(--orange)); }
  .band__cool { flex: 1; background: linear-gradient(90deg, var(--silver-dark), var(--silver) 40%, #ffffff 70%, var(--silver)); }
</style>
</head>
<body>

  <section class="card card--logo" aria-label="Business card, logo side">
    <div class="tab tab--top"></div>
    <div class="tab tab--bottom"></div>
    <div class="brand">
      <div class="brand__row">
        <span class="brand__dot"></span>
        <span class="brand__name">Gilded Critters</span>
      </div>
      <span class="brand__url">www.gildedcritters.example</span>
    </div>
  </section>

  <section class="card card--contact" aria-label="Business card, contact side">
    <div class="brand">
      <div class="brand__row">
        <span class="brand__dot"></span>
        <span class="brand__name">Gilded Critters</span>
      </div>
      <span class="brand__url">www.gildedcritters.example</span>
    </div>

    <div class="person">
      <h1 class="person__name">Daniel <strong>Workby</strong></h1>
      <p class="person__role">Sales and Marketing</p>
    </div>

    <ul class="contacts">
      <li>530-471-6328
        <span class="icon"><svg viewBox="0 0 24 24"><path fill="#fff" d="M6.6 10.8a15 15 0 0 0 6.6 6.6l2.2-2.2a1 1 0 0 1 1-.25 11.4 11.4 0 0 0 3.6.57 1 1 0 0 1 1 1V20a1 1 0 0 1-1 1A17 17 0 0 1 3 4a1 1 0 0 1 1-1h3.5a1 1 0 0 1 1 1c0 1.25.2 2.45.57 3.57a1 1 0 0 1-.25 1z"/></svg></span>
      </li>
      <li>info@gildedcritters.example
        <span class="icon"><svg viewBox="0 0 24 24"><rect x="3" y="6" width="18" height="12" rx="1" fill="none" stroke="#fff" stroke-width="2"/><path d="M3 7l9 6 9-6" fill="none" stroke="#fff" stroke-width="2"/></svg></span>
      </li>
      <li>www.gildedcritters.example
        <span class="icon"><svg viewBox="0 0 24 24"><path fill="#fff" d="M6 3l13 8-6 1.5 3.5 6.5-2.5 1.3-3.5-6.5L6 18z"/></svg></span>
      </li>
      <li>gilded critters
        <span class="icons"><span class="icon icon--social"></span><span class="icon icon--social"></span></span>
      </li>
    </ul>

    <div class="band"><span class="band__warm"></span><span class="band__cool"></span></div>
  </section>

</body>
</html>
```